SHT Vision Campaign Doc

We need to update and redesign a document done 5 years ago. It must look different, more professional and less like a slideshow. The document is uploaded called Keystone 2025. The new document will be called Keystone 2030. And while it's the same organization, we want to improve on the graphic design. I have also uploaded all the new text for the updated 2030 document. The campaign logo is also uploaded. It can only be used on a white background.

Target Market(s)

Donors to the silver harbour trust

Industry/Entity Type

non-profit

Font styles to use
Sans Serif
Other font styles liked:
• Neue Haas Unica

Colors
EB3D1F
EC4F4E
F09395
F8D3D4
FCEDEE

Requirements
Must have
• Neue Haas Unica typeface
Nice to have
• images that match the content. They talk about 4 pillars. Would be nice to show those - BUT not greek style pillars. More like graphs

```html
<!DOCTYPE html>
<html lang="en">
<head>
<meta charset="utf-8">
<title>Keystone 2030 Summary – Cover Spread</title>
<link rel="stylesheet" href="https://fonts.googleapis.com/css2?family=Inter:wght@400;500;600;700&display=swap">
<style>
  :root {
    --bg: #d0d0d0;
    --red-deep: #dc0d16;
    --red-main: #e01c26;
    --red-soft: #e5505a;
    --white: #ffffff;
    --band: #f1f0f0;
    --map-red: #e63a3f;
    --map-light: #f6d6d6;
  }
  * { box-sizing: border-box; margin: 0; padding: 0; }
  html, body { width: 1200px; height: 1200px; overflow: hidden; }
  body {
    background: var(--bg);
    font-family: "Inter", sans-serif;
    display: flex;
    align-items: center;
    justify-content: center;
  }
  .spread {
    display: flex;
    width: 1116px;
    height: 580px;
    box-shadow: 0 18px 40px rgba(0,0,0,0.18);
  }
  .back-cover {
    position: relative;
    width: 540px;
    height: 100%;
    background: var(--red-deep);
  }
  .contact {
    position: absolute;
    left: 44px;
    bottom: 44px;
    color: var(--white);
  }
  .contact-title {
    font-size: 13px;
    font-weight: 600;
    letter-spacing: 0.02em;
    margin-bottom: 10px;
  }
  .contact-icons {
    display: flex;
    gap: 12px;
    align-items: center;
  }
  .contact-icons .dot {
    width: 16px;
    height: 16px;
    border-radius: 50%;
    background: var(--white);
  }
  .contact-icons svg { width: 18px; height: 18px; display: block; }

  .spine {
    width: 36px;
    height: 100%;
    background: var(--red-deep);
    display: flex;
    flex-direction: column;
    border-left: 1px solid rgba(0,0,0,0.08);
    border-right: 1px solid rgba(0,0,0,0.08);
  }
  .spine-segment {
    display: flex;
    align-items: center;
    justify-content: center;
    writing-mode: vertical-rl;
    font-size: 11px;
    font-weight: 700;
    letter-spacing: 0.08em;
    text-transform: uppercase;
    color: var(--white);
  }
  .spine-title { flex: 0 0 250px; }
  .spine-date { flex: 0 0 150px; background: var(--white); color: var(--red-deep); }
  .spine-version { flex: 0 0 100px; }

  .front-cover {
    position: relative;
    width: 540px;
    height: 100%;
    background: linear-gradient(115deg, var(--red-main) 0%, var(--red-main) 35%, var(--red-soft) 100%);
    overflow: hidden;
  }
  .brand {
    position: absolute;
    top: 34px;
    right: 34px;
    display: flex;
    align-items: center;
    gap: 8px;
    color: var(--white);
    font-size: 12px;
    font-weight: 600;
    line-height: 1.2;
    text-align: right;
  }
  .brand-mark {
    width: 22px;
    height: 22px;
    border-radius: 50%;
    background: var(--white);
  }
  .cover-band {
    position: absolute;
    left: 0;
    right: 0;
    top: 190px;
    height: 175px;
    background: var(--band);
  }
  .cover-art {
    position: absolute;
    left: 160px;
    top: 130px;
    width: 280px;
    height: 220px;
    border-radius: 40% 40% 30% 30%;
    background: radial-gradient(ellipse at 45% 40%, var(--map-red) 0%, var(--map-red) 35%, var(--map-light) 75%, rgba(246,214,214,0) 100%);
  }
  .cover-meta {
    position: absolute;
    left: 44px;
    bottom: 40px;
    color: var(--white);
    font-size: 13px;
    font-weight: 500;
    line-height: 1.4;
  }
</style>
</head>
<body>
  <main class="spread">
    <section class="back-cover">
      <div class="contact">
        <p class="contact-title">GET IN TOUCH</p>
        <div class="contact-icons">
          <span class="dot"></span>
          <span class="dot"></span>
          <span class="dot"></span>
          <span class="dot"></span>
          <svg viewBox="0 0 20 20" aria-label="Website">
            <g fill="none" stroke="#fff" stroke-width="1.4">
              <circle cx="10" cy="10" r="8"/>
              <ellipse cx="10" cy="10" rx="3.5" ry="8"/>
              <line x1="2" y1="10" x2="18" y2="10"/>
            </g>
          </svg>
          <svg viewBox="0 0 20 20" aria-label="Email">
            <g fill="none" stroke="#fff" stroke-width="1.4">
              <rect x="2" y="4" width="16" height="12"/>
              <polyline points="2,4 10,11 18,4"/>
            </g>
          </svg>
        </div>
      </div>
    </section>

    <aside class="spine">
      <div class="spine-segment spine-title">Keystone 2030 Summary</div>
      <div class="spine-segment spine-date">March 17, 2025</div>
      <div class="spine-segment spine-version">Version 8</div>
    </aside>

    <section class="front-cover">
      <div class="brand">
        <span>Silver Harbour Trust<br>Keystone 2030</span>
        <span class="brand-mark"></span>
      </div>
      <div class="cover-band"></div>
      <div class="cover-art" role="img" aria-label="Red and white map of the country with a location pin marking the organization's reach"></div>
      <div class="cover-meta">
        <p>Keystone 2030 summary</p>
        <p>March 17, 2025</p>
        <p>version 8</p>
      </div>
    </section>
  </main>
</body>
</html>
```